Northwind Insight Partners needs a PowerPoint Flow Chart Design

We are a market research company based in ChicagoWe need a Powerpoint design for a new market research process to demonstrate the system using a flow chart which needs to be illustrated in a series of slides for presentations , videos etc. as well as being summarized in one chart if possible - There are c 12 "sections" to this flow chart in order of sequence
We are looking for a demonstration of our process which should be clear, logical with creative dynamism (we are not accountants!) I attach our logo ideally this should be on every slide plus if possible use those colors

Target Market(s)

Senior managers in large global corporations

Industry/Entity Type

Market Research

Requirements
Must have
• Clear - Logical - Dynamic
Should be able to show whole process and then break it down into individual stages in a clear flow diagram

See attached document as guideline

```html
<!DOCTYPE html>
<html lang="en">
<head>
<meta charset="utf-8">
<title>Business Profile – Process Cycle</title>
<link rel="stylesheet" href="https://fonts.googleapis.com/css2?family=Roboto:wght@400;700;900&display=swap">
<style>
  :root {
    --bg: #f7f8fc;
    --brand-blue: #1f64b4;
    --bar-blue: #2f6db5;
    --bar-navy: #27478a;
    --bar-maroon: #7e1a24;
    --bar-red: #b0202a;
    --bar-bright: #d6262d;
    --heading-red: #d4232b;
    --body-grey: #a9a9ab;
    --cycle-blue: #1b66b0;
    --ring-grey: #dcdcde;
    --stripe: #cfd0d4;
    --white: #ffffff;
  }
  * { margin: 0; padding: 0; box-sizing: border-box; }
  html, body { width: 1200px; height: 900px; overflow: hidden; }
  body {
    position: relative;
    background: var(--bg);
    font-family: "Roboto", Arial, sans-serif;
  }
  .top-bar {
    position: absolute; top: 0; left: 0; width: 1200px; height: 10px;
    display: flex;
  }
  .top-bar span { flex: 1; }
  .top-bar .c1 { background: var(--bar-blue); }
  .top-bar .c2 { background: var(--bar-navy); }
  .top-bar .c3 { background: var(--bar-maroon); }
  .top-bar .c4 { background: var(--bar-red); }
  .top-bar .c5 { background: var(--bar-bright); }

  .intro { position: absolute; left: 70px; top: 54px; width: 1082px; }
  .section-title {
    font-size: 22px; font-weight: 700; color: var(--brand-blue);
    line-height: 32px; margin-bottom: 8px;
  }
  .section-title.accent { color: var(--heading-red); }
  .section-text {
    font-size: 19.5px; line-height: 33px; color: var(--body-grey);
    text-align: justify;
  }
  .detail { position: absolute; left: 567px; top: 432px; width: 578px; }
  .detail .section-title { margin-bottom: 2px; }
  .detail .section-text { text-align: left; }

  .cycle { position: absolute; left: 80px; top: 322px; width: 420px; height: 420px; }
  .cycle-shadow {
    position: absolute; left: 170px; top: 730px; width: 240px; height: 24px;
    border-radius: 50%;
    background: radial-gradient(ellipse at center, rgba(90,90,90,.45) 0%, rgba(90,90,90,0) 70%);
  }
  .cycle .step { fill: var(--cycle-blue); stroke: var(--white); stroke-width: 2; }
  .cycle .ring { fill: var(--white); stroke: var(--ring-grey); stroke-width: 14; }
  .cycle .label {
    fill: var(--white); font-family: "Roboto", Arial, sans-serif;
    font-weight: 900; font-size: 19px; letter-spacing: 1px;
  }

  .footer-band {
    position: absolute; left: 0; bottom: 0; width: 1200px; height: 48px;
    background: repeating-linear-gradient(90deg, var(--stripe) 0 2px, var(--bg) 2px 5px);
  }
  .brand-tag {
    position: absolute; right: 4px; bottom: 3px; width: 80px; height: 42px;
    background: var(--white);
    display: flex; align-items: center; justify-content: center; text-align: center;
    font-size: 10px; line-height: 12px; font-weight: 700; color: var(--brand-blue);
  }
</style>
</head>
<body>
  <div class="top-bar"><span class="c1"></span><span class="c2"></span><span class="c3"></span><span class="c4"></span><span class="c5"></span></div>

  <section class="intro">
    <h1 class="section-title">Business Profile Title Here</h1>
    <p class="section-text">Subtext here Subtext here Subtext here Subtext here Subtext here Subtext here Subtext here Subtext here Subtext here Subtext here Subtext here Subtext here Subtext here Subtext here Subtext here Subtext here Subtext here Subtext here Subtext here Subtext here Subtext here Subtext here Subtext here Subtext here Subtext here Subtext here Subtext here Subtext here Subtext here Subtext here Subtext here Subtext here Subtext here Subtext here Subtext here</p>
  </section>

  <div class="cycle-shadow"></div>
  <svg class="cycle" viewBox="0 0 400 400" role="img" aria-label="Process cycle: Explore, Change, Grow, Renew">
    <defs>
      <path id="step-shape" d="M25.1 193.9 A175 175 0 0 1 175.6 26.7 L173.6 11.8 L218.3 51.1 L184.7 91.1 L182.6 76.2 A125 125 0 0 0 75.1 195.6 L52.3 174.0 Z"/>
    </defs>
    <use href="#step-shape" class="step"/>
    <use href="#step-shape" class="step" transform="rotate(90 200 200)"/>
    <use href="#step-shape" class="step" transform="rotate(180 200 200)"/>
    <use href="#step-shape" class="step" transform="rotate(270 200 200)"/>
    <circle class="ring" cx="200" cy="200" r="68"/>
    <text class="label" x="94" y="94" text-anchor="middle" dominant-baseline="central" transform="rotate(-45 94 94)">EXPLORE</text>
    <text class="label" x="306" y="94" text-anchor="middle" dominant-baseline="central" transform="rotate(45 306 94)">CHANGE</text>
    <text class="label" x="306" y="306" text-anchor="middle" dominant-baseline="central" transform="rotate(-45 306 306)">GROW</text>
    <text class="label" x="94" y="306" text-anchor="middle" dominant-baseline="central" transform="rotate(45 94 306)">RENEW</text>
  </svg>

  <section class="detail">
    <h2 class="section-title accent">Business Profile Title Here</h2>
    <p class="section-text">Subtext here Subtext here Subtext here Subtext here Subtext here Subtext here Subtext here Subtext here Subtext here Subtext here Subtext here Subtext here Subtext here Subtext here Subtext here Subtext here Subtext here Subtext here Subtext here Subtext here Subtext here Subtext here Subtext here Subtext here Subtext here Subtext here Subtext here Subtext here Subtext here Subtext here Subtext here Subtext here</p>
  </section>

  <footer class="footer-band">
    <div class="brand-tag">Northwind Insight Partners</div>
  </footer>
</body>
</html>
```